Single brochure for international companies in the financial sector

We need to update a brochure 4 pages presenting our company. We are a financial engineering company. The final design must provide financial security, service and trust. you will find the current brochure copy. Our color code is Orange (RGB 235/100/68), Black, White and Gray. photos show the visual of the site, but it is not mandatory to keep them.

Target Market(s)

wealth management professionals

Industry/Entity Type

Finance

Requirements
Must have
• Logo Velbrook Capital all text in the document color Orange Velbrook (RGB 235/100/68)
Nice to have
• Vista Font
Should not have
• images / pictures of people

```html
<!DOCTYPE html>
<html lang="en">
<head>
<meta charset="utf-8">
<title>Velbrook Capital – Brochure Covers</title>
<link rel="stylesheet" href="https://fonts.googleapis.com/css2?family=Anton&family=Jost:wght@300;400&family=Lato:wght@400&display=swap">
<style>
  :root {
    --orange: #eb6444;
    --orange-soft: #f39a80;
    --orange-pale: #f8c4b2;
    --black: #1f1f1f;
    --ink: #262626;
    --white: #ffffff;
    --gray: #8a8a8a;
  }
  * { margin: 0; padding: 0; box-sizing: border-box; }
  html, body { width: 1200px; height: 758px; overflow: hidden; background: var(--white); }
  .canvas { position: relative; width: 1200px; height: 758px; background: var(--white); }

  .page {
    position: absolute; top: 87px; width: 460px; height: 594px; overflow: hidden;
    box-shadow: 0 3px 10px rgba(0,0,0,.35);
  }

  /* Back cover */
  .back-cover { left: 93px; background: var(--orange); }
  .back-cover .visual {
    position: absolute; left: 0; top: 0; width: 100%; height: 335px;
    background: linear-gradient(180deg, var(--orange-pale) 0%, var(--orange-soft) 45%, var(--orange) 100%);
  }
  .back-cover .name-block {
    position: absolute; left: 22px; top: 456px; width: 168px;
    font-family: "Jost", sans-serif; font-weight: 300; color: var(--ink); text-align: center;
  }
  .back-cover .name-main { font-size: 20px; letter-spacing: 8px; margin-right: -8px; line-height: 24px; }
  .back-cover .name-sub { font-size: 14px; letter-spacing: 5px; margin-right: -5px; line-height: 18px; margin-top: 2px; }
  .back-cover .divider {
    position: absolute; left: 214px; top: 425px; width: 1px; height: 104px;
    background: rgba(150,60,40,.45);
  }
  .back-cover .company-details {
    position: absolute; left: 240px; top: 440px;
    font-family: "Lato", sans-serif; color: var(--white); font-size: 10.5px; line-height: 17.5px;
  }
  .back-cover .company-details .phone { font-size: 14px; margin-top: 4px; }
  .url-band {
    position: absolute; left: 0; bottom: 0; width: 100%; height: 31px;
    font-family: "Lato", sans-serif; font-size: 12px; letter-spacing: 6px; color: var(--white);
    display: flex; align-items: center; justify-content: center;
  }
  .back-cover .url-band { background: var(--black); }

  /* Front cover */
  .front-cover { left: 633px; background: var(--white); }
  .front-cover .name-block {
    position: absolute; left: 0; top: 63px; width: 100%; text-align: center;
    font-family: "Jost", sans-serif; font-weight: 300; color: var(--orange);
  }
  .front-cover .name-main { font-size: 28px; letter-spacing: 14px; margin-right: -14px; line-height: 30px; }
  .front-cover .name-sub { font-size: 19px; letter-spacing: 6px; margin-right: -6px; line-height: 22px; margin-top: 9px; }
  .front-cover .visual {
    position: absolute; left: 0; top: 135px; width: 100%; height: 265px;
    background: linear-gradient(110deg, #5d7186 0%, #b9c3cc 42%, var(--orange-pale) 58%, var(--orange-soft) 80%, var(--orange) 100%);
  }
  .front-cover .headline { position: absolute; left: 0; top: 418px; width: 460px; height: 136px; }
  .front-cover .url-band { background: var(--orange); }
</style>
</head>
<body>
<main class="canvas">

  <section class="page back-cover">
    <div class="visual" role="img" aria-label="Orange-toned photo of a hard hat and rolled plans on a desk in front of a city construction site with cranes"></div>
    <div class="name-block">
      <div class="name-main">VELBROOK</div>
      <div class="name-sub">CAPITAL</div>
    </div>
    <div class="divider"></div>
    <div class="company-details">
      <p>Velbrook Capital SA. Capital : 400 000 Euros</p>
      <p>RCS Paris : 812 455 103</p>
      <p>Code Banque (CIB) : 14720</p>
      <p class="phone">Tel : +33 1 47 20 58 16</p>
    </div>
    <div class="url-band">www.velbrookcapital.com</div>
  </section>

  <section class="page front-cover">
    <div class="name-block">
      <div class="name-main">VELBROOK</div>
      <div class="name-sub">CAPITAL</div>
    </div>
    <div class="visual" role="img" aria-label="Construction site photo with steel framework and a crane, blending into orange on the right"></div>
    <svg class="headline" viewBox="0 0 460 136" width="460" height="136">
      <defs>
        <linearGradient id="headline-split" gradientUnits="userSpaceOnUse" x1="207" y1="-136" x2="255" y2="212">
          <stop offset="0.5" stop-color="#eb6444"/>
          <stop offset="0.5" stop-color="#1f1f1f"/>
        </linearGradient>
      </defs>
      <text x="57" y="67" textLength="349" lengthAdjust="spacingAndGlyphs"
            font-family="Anton, sans-serif" font-size="65" fill="url(#headline-split)">FINANCIAL</text>
      <text x="55" y="119" textLength="351" lengthAdjust="spacingAndGlyphs"
            font-family="Jost, sans-serif" font-weight="400" font-size="56" fill="#1f1f1f">ENGINEERING</text>
    </svg>
    <div class="url-band">www.velbrookcapital.com</div>
  </section>

</main>
</body>
</html>
```